Fashion Design Business Card

I need a new business card designed for a new fashion company. I have attached what I have currently designed. I want it more feminine looking, the logo needs to be gold. I want it simple, feminine and stylish. Please give me some different ideas with the fonts.
Updates

I need to send the design we currently have, as we have worked out the logo.
You also need all of our details
Industry/Entity Type
Fashion
Look and feel
Each slider illustrates characteristics of the customer's brand and the style your logo design should communicate.

```html
<!DOCTYPE html>
<html lang="en">
<head>
<meta charset="utf-8">
<title>Mira Valen – Business Card</title>
<link href="https://fonts.googleapis.com/css2?family=Cantarell:wght@400;700&family=Dancing+Script:wght@700&display=swap" rel="stylesheet">
<style>
  :root {
    --backdrop-light: #2a2a2a;
    --backdrop-dark: #121212;
    --card-lilac: #7e7a9e;
    --card-mist: #c9c6dc;
    --card-white: #ffffff;
    --card-cream: #f3ead9;
    --name-red: #8a1f1a;
    --title-red: #a3140e;
    --contact-grey: #4a4652;
    --gold: #c9961f;
    --sun-yellow: #ffdf00;
    --back-white: #ffffff;
  }
  * { margin: 0; padding: 0; box-sizing: border-box; }
  html, body { width: 1200px; height: 900px; overflow: hidden; }
  body {
    background: radial-gradient(ellipse at 50% 35%, var(--backdrop-light) 0%, var(--backdrop-dark) 80%);
    font-family: "Cantarell", sans-serif;
    position: relative;
  }
  .card {
    position: absolute;
    top: 200px;
    width: 557px;
    height: 313px;
    border-radius: 18px;
    overflow: hidden;
  }
  .card-front {
    left: 39px;
    background:
      radial-gradient(ellipse 60% 65% at 48% 42%, var(--card-white) 0%, var(--card-cream) 35%, var(--card-mist) 75%, var(--card-lilac) 100%);
  }
  .card-back {
    left: 614px;
    background: var(--sun-yellow);
    display: flex;
    align-items: center;
    justify-content: center;
  }
  .brand-mark {
    position: absolute;
    left: 40px;
    top: 82px;
    display: flex;
    align-items: center;
    gap: 10px;
    color: var(--gold);
    font-weight: 700;
    font-size: 22px;
  }
  .brand-dot {
    width: 26px;
    height: 26px;
    border-radius: 50%;
    background: var(--gold);
  }
  .holder-name {
    position: absolute;
    left: 207px;
    top: 68px;
    color: var(--name-red);
    font-size: 29px;
    letter-spacing: 1px;
    font-weight: 400;
  }
  .holder-title {
    position: absolute;
    left: 285px;
    top: 104px;
    color: var(--title-red);
    font-family: "Dancing Script", cursive;
    font-weight: 700;
    font-size: 20px;
  }
  .contact-list {
    position: absolute;
    left: 262px;
    top: 225px;
    list-style: none;
    color: var(--contact-grey);
    font-size: 16px;
    line-height: 21px;
  }
  .back-name {
    color: var(--back-white);
    font-weight: 700;
    font-size: 64px;
  }
</style>
</head>
<body>
  <section class="card card-front">
    <div class="brand-mark"><span class="brand-dot"></span>Mira Valen</div>
    <h1 class="holder-name">MIRA&nbsp; VALEN</h1>
    <p class="holder-title">fashion designer</p>
    <ul class="contact-list">
      <li>PHONE: 0400512736</li>
      <li>Email:&nbsp; mira@miravalen.com</li>
      <li>Web:&nbsp; www.miravalen.com</li>
    </ul>
  </section>
  <section class="card card-back">
    <p class="back-name">Mira Valen</p>
  </section>
</body>
</html>
```